Home page design layout for commercial driving school

- This is for a layout design of the home page only. No coding required.

- The design must be based around the attached HPID (home page information design). The table boxes are just for approximate placement of information – you DON'T have to make it look exactly like this. Information only is in orange text. Copy to go on the design in black text. Some instructions are in the HPID. Please be creative! You don’t have to use the exact images provided if you have a better idea.

- The design needs to be professional and modern. Fonts used except in the header must be Google fonts.

I've attached:
- HPID (information design) as a Word doc and PDF
- the logo. Please use the colours from the logos in the website design. Lots of white too.
- images for the gallery
- icon examples for the buttons for under the gallery - these aren't high resolution. If you have access to better examples please use those instead.
- logos of accreditations for that section
- background image that you may or may not use. This image is used in the business folders and business cards and I've got an example in this folder. If you can incorporate this into the design you may but it's not compulsory.

The winning PSD file will have to be provided as follows…
1. Canvas size of 2000px x 2000px - 72ppi in Adobe Photoshop (CS5 compatible)
2. Width of content section is 1100px wide - centered in the canvas
3. Header height (without nav bar) 150-160 pixels.
4. Any button rollovers/hovers in the PSD as hidden layers.
5. All fonts used must be Google fonts (except for the header fonts).
6. You will need to supply the chosen home page plus one example page (example page as a style guide for how all other pages will look). Example page is only the header and navigational bar at the top, an empty sector in the middle with a column (180 px wide) which can be left or right aligned which means the main sector is 920 pixels wide, and then the footer at the bottom of the page.

Apologies for the delay in assigning a first place for this project. We will be completing this project as soon as we can.

```html
<!DOCTYPE html>
<html lang="en">
<head>
<meta charset="utf-8">
<title>Summit Drive Academy – Home</title>
<link href="https://fonts.googleapis.com/css2?family=Tinos:ital,wght@1,400;1,700&family=Open+Sans:wght@400;600;700&display=swap" rel="stylesheet">
<style>
:root{
  --blue:#1f5ea8;
  --blue-bright:#2a8cf2;
  --blue-dark:#14407a;
  --sky:#cfe1f7;
  --green:#63d46a;
  --green-dark:#2f8a36;
  --ink:#222;
  --muted:#888;
  --white:#fff;
}
*{box-sizing:border-box;margin:0;padding:0}
html,body{width:1200px;height:900px;overflow:hidden;background:var(--white);font-family:"Open Sans",sans-serif;color:var(--ink)}
.page{position:absolute;left:351px;top:0;width:497px;height:900px}
.abs{position:absolute}

/* header */
.header{left:0;top:0;width:497px;height:72px;background:linear-gradient(90deg,#9fc4f0,#e6f0fc 40%);overflow:hidden}
.header-swoosh{left:148px;top:-40px;width:420px;height:112px;background:var(--white);border-radius:90px 0 0 0}
.brand-mark{left:14px;top:10px;width:52px;height:52px;border-radius:50%;background:var(--blue);border:3px solid var(--white);box-shadow:0 0 0 1px var(--blue)}
.brand-name{left:8px;top:64px;font-size:5px;font-weight:700;color:var(--blue);display:none}
.map-fill{left:78px;top:8px;width:42px;height:58px;background:linear-gradient(#e9eef5,#c8d2de);border-radius:40% 30% 50% 40%}
.title{right:0;top:4px;font-family:"Tinos",serif;font-style:italic;font-size:15.5px;color:var(--blue)}
.subtitle{right:0;top:23px;font-size:6.3px;color:var(--blue)}
.registered{right:6px;top:31px;font-size:6.3px;font-weight:700;color:var(--blue-dark)}
.motto{right:0;top:52px;font-family:"Tinos",serif;font-style:italic;font-weight:700;font-size:12px;color:var(--blue-dark)}

/* nav */
.nav{left:0;top:73px;width:497px;height:17px;background:linear-gradient(#3a97f5,var(--blue-bright));display:flex;align-items:center}
.nav-home{width:41px;height:17px;background:#0a0a0a;display:flex;align-items:center;justify-content:center}
.nav ul{list-style:none;display:flex;flex:1;justify-content:space-around}
.nav li{font-size:6.3px;font-weight:700;color:var(--white)}

/* hero */
.hero{left:0;top:90px;width:497px;height:213px;background:var(--blue-bright);border-radius:0 0 5px 5px}
.hero-photo{left:4px;top:0;width:490px;height:179px;background:linear-gradient(#9db9dc 0%,#c5d8ec 30%,#5b7350 55%,#7a8773 70%,#66696c 100%)}
.hero-text{left:60px;top:184px;width:200px;text-align:center;font-size:8.5px;line-height:10px;color:var(--white)}
.hero-btn{left:305px;top:187px;width:69px;height:18px;background:linear-gradient(#8be88f,var(--green));border:1px solid #3fb046;border-radius:2px;color:var(--green-dark);font-size:8.5px;font-weight:700;display:flex;align-items:center;justify-content:center;letter-spacing:.5px}

/* course buttons */
.course{width:88px;height:60px}
.course svg{position:absolute;left:24px;top:0;width:40px;height:32px}
.course-label{position:absolute;left:0;bottom:0;width:88px;height:24px;background:var(--blue);border-top:1px solid #5d8fd0;color:var(--white);font-size:5.4px;font-weight:700;text-align:center;display:flex;align-items:center;justify-content:center;line-height:6.5px;padding:0 3px}

/* info cards */
.card{top:516px;width:159px;height:124px;border:1px solid #ccc;border-radius:3px;padding:8px 5px}
.card h2{font-size:7px;font-weight:700;margin-bottom:8px}
.card p{font-size:5.6px;font-weight:600;line-height:7px;margin-bottom:7px}
.card ul{list-style:none}
.card li{font-size:5.6px;line-height:6.6px;margin-bottom:4px;padding-left:8px;position:relative}
.card li::before{content:"";position:absolute;left:0;top:1px;width:4px;height:4px;border-radius:50%;background:var(--green-dark)}
.card.faq li{color:var(--blue)}
.more{position:absolute;right:0;bottom:0;width:56px;height:10px;background:#8fb3cf;color:var(--white);font-size:5.4px;display:flex;align-items:center;padding-left:2px}
.more::after{content:"";position:absolute;right:2px;top:2px;border-left:5px solid #b9e03a;border-top:3px solid transparent;border-bottom:3px solid transparent}

/* partners */
.badge{height:20px;border-radius:2px}

/* footer */
.footer{left:0;top:732px;width:497px;height:152px;border-top:2px solid #ddd;box-shadow:0 -1px 3px rgba(0,0,0,.08)}
.foot-col{font-size:5.6px;line-height:11px}
.foot-col strong{font-weight:600;display:block}
.foot-col .sub{padding-left:12px}
.foot-rule{width:1px;height:100px;background:linear-gradient(transparent,#777,transparent)}
.foot-map{left:337px;top:64px;width:160px;height:82px;background:linear-gradient(135deg,#aac4e2,#d5e0c7 45%,#b0cbe6)}
.copyright{left:0;top:884px;width:497px;height:16px;background:var(--blue);color:#8fb0db;font-size:5.4px;display:flex;align-items:center;justify-content:center}
</style>
</head>
<body>
<div class="page">

  <header class="abs header">
    <div class="abs header-swoosh"></div>
    <div class="abs brand-mark" aria-hidden="true"></div>
    <div class="abs map-fill" role="img" aria-label="Outline map of New Zealand"></div>
    <h1 class="abs title">Driver, driving instructor &amp; driver assessor education &amp; training</h1>
    <p class="abs subtitle">Vehicle types include: heavy vehicles, light fleet vehicles, buses, forklifts and specialist machines</p>
    <p class="abs registered">Registered with NQB and Regional Transport Authority Approved Training Provider</p>
    <p class="abs motto">“Upskilling drivers to be professional, safe and efficient”</p>
  </header>

  <nav class="abs nav">
    <div class="nav-home">
      <svg width="10" height="9" viewBox="0 0 10 9"><path d="M5 0 10 4.5H8.5V9H6V6H4V9H1.5V4.5H0Z" fill="#fff"/></svg>
    </div>
    <ul><li>ABOUT</li><li>COURSES</li><li>LOCATION</li><li>RESOURCES</li><li>LINKS</li><li>FAQ</li><li>CONTACT</li></ul>
  </nav>

  <section class="abs hero">
    <div class="abs hero-photo" role="img" aria-label="Summit Drive Academy training tanker truck on a test track"></div>
    <p class="abs hero-text">Improve safety and compliance and reduce vehicle operating costs for our clients.</p>
    <div class="abs hero-btn">DRIVE</div>
  </section>

  <!-- course buttons row 1 -->
  <div class="abs course" style="left:12px;top:333px">
    <svg viewBox="0 0 40 32"><rect x="8" y="4" width="24" height="26" fill="none" stroke="#1f5ea8" stroke-width="2.5"/><path d="M12 16l6 7L36 1" fill="none" stroke="#1f5ea8" stroke-width="3"/></svg>
    <div class="course-label">RTA Approved<br>Driver License</div>
  </div>
  <div class="abs course" style="left:107px;top:333px">
    <svg viewBox="0 0 40 32"><rect x="14" y="8" width="24" height="18" fill="#1f5ea8"/><path d="M2 26V16l4-6h7v16Z" fill="#1f5ea8"/><circle cx="8" cy="28" r="3" fill="#1f5ea8"/><circle cx="28" cy="28" r="3" fill="#1f5ea8"/><circle cx="34" cy="28" r="3" fill="#1f5ea8"/></svg>
    <div class="course-label">Heavy Vehicle</div>
  </div>
  <div class="abs course" style="left:202px;top:333px">
    <svg viewBox="0 0 40 32"><path d="M2 28V18l6-6h30v16Z" fill="#1f5ea8"/><circle cx="10" cy="29" r="3" fill="#1f5ea8"/><circle cx="30" cy="29" r="3" fill="#1f5ea8"/></svg>
    <div class="course-label">Light Vehicle Fleets</div>
  </div>
  <div class="abs course" style="left:297px;top:333px">
    <svg viewBox="0 0 40 32"><path d="M8 4h3v24H8ZM11 24h12v3H11ZM24 8h10v18H24Z" fill="#1f5ea8"/><circle cx="27" cy="29" r="3" fill="#1f5ea8"/></svg>
    <div class="course-label">Forklifts</div>
  </div>
  <div class="abs course" style="left:392px;top:333px">
    <svg viewBox="0 0 40 32"><path d="M4 20h32v6H4Z" fill="#1f5ea8"/><path d="M12 20 20 4l8 4-6 12Z" fill="#1f5ea8"/><circle cx="10" cy="28" r="3" fill="#1f5ea8"/><circle cx="30" cy="28" r="3" fill="#1f5ea8"/></svg>
    <div class="course-label">Plant &amp; Telehandler</div>
  </div>

  <!-- course buttons row 2 -->
  <div class="abs course" style="left:12px;top:429px">
    <svg viewBox="0 0 40 32"><rect x="8" y="2" width="24" height="4" fill="#1f5ea8"/><path d="M10 6l20 8M30 6 10 14M10 14l20 8M30 14 10 22" stroke="#1f5ea8" stroke-width="2.5"/><rect x="8" y="22" width="24" height="5" fill="#1f5ea8"/></svg>
    <div class="course-label">Elevated Work Platforms /<br>Scissor Lifts</div>
  </div>
  <div class="abs course" style="left:107px;top:429px">
    <svg viewBox="0 0 40 32"><rect x="6" y="2" width="14" height="12" fill="#1f5ea8"/><circle cx="26" cy="14" r="4" fill="#1f5ea8"/><path d="M18 30v-8q8-6 16 0v8Z" fill="#1f5ea8"/></svg>
    <div class="course-label">Driving Instructors &amp;<br>Assessors</div>
  </div>
  <div class="abs course" style="left:202px;top:429px">
    <svg viewBox="0 0 40 32"><rect x="1" y="6" width="38" height="20" rx="3" fill="#1f5ea8"/><path d="M4 10h6v6H4ZM12 10h6v6h-6ZM20 10h6v6h-6ZM28 10h8v6h-8Z" fill="#fff"/><circle cx="9" cy="27" r="3" fill="#1f5ea8"/><circle cx="31" cy="27" r="3" fill="#1f5ea8"/></svg>
    <div class="course-label">Bus, Coach &amp; Taxi</div>
  </div>
  <div class="abs course" style="left:297px;top:429px">
    <svg viewBox="0 0 40 32"><text x="20" y="24" text-anchor="middle" font-family="Open Sans,sans-serif" font-weight="700" font-size="18" fill="#1f5ea8">4X4</text></svg>
    <div class="course-label">Four Wheel Drive &amp;<br>Quads</div>
  </div>
  <div class="abs course" style="left:392px;top:429px">
    <svg viewBox="0 0 40 32"><path d="M20 2 36 16 20 30 4 16Z" fill="#1f5ea8"/><path d="M6 12h28M4 16h32M6 20h28" stroke="#fff" stroke-width="1.5"/></svg>
    <div class="course-label">HazSub Approved Handler /<br>Filler Dangerous Goods<br>Handling</div>
  </div>

  <!-- info cards -->
  <section class="abs card" style="left:1px">
    <h2>Summit Drive Academy is registered with:</h2>
    <ul>
      <li>NQB as a PTE (Private Training Establishment)</li>
      <li>Regional Transport Authority for approved licence courses</li>
      <li>Regional Transport Authority for approved licence courses</li>
      <li>Trade Skills ITO/ SafeWork Council for forklift training</li>
      <li>HPO for HazSub Certification</li>
      <li>Department of Transit / Regional Transport Authority for SafeDrive driver &amp; instructor courses</li>
    </ul>
    <span class="more">FIND OUT MORE</span>
  </section>
  <section class="abs card faq" style="left:168px">
    <h2>Summit Drive Courses FAQs</h2>
    <p>Find out the answers to the most often asked questions about Summit Drive courses here...</p>
    <ul>
      <li>Does Summit Drive run courses in my location?</li>
      <li>Do you have advanced driving courses?</li>
      <li>What accreditation will your (course name) give me?</li>
      <li>How much does the course I want to do cost?</li>
    </ul>
    <span class="more">FIND OUT MORE</span>
  </section>
  <section class="abs card" style="left:335px">
    <h2>Summit Drive Courses by Location</h2>
    <ul>
      <li>Summit Drive run courses throughout New Zealand.</li>
      <li>You can find courses by location and enrol online.</li>
      <li>If you can't find the course you want in your area, please contact us as we can run any course in any location (conditions may apply).</li>
    </ul>
    <span class="more">FIND OUT MORE</span>
  </section>

  <!-- accreditation partners -->
  <div class="abs badge" style="left:52px;top:659px;width:46px;background:#dfe6f4"></div>
  <div class="abs badge" style="left:107px;top:662px;width:46px;background:#f4dcdc"></div>
  <div class="abs badge" style="left:162px;top:657px;width:47px;background:#2a3c55"></div>
  <div class="abs badge" style="left:217px;top:658px;width:51px;background:#222"></div>
  <div class="abs badge" style="left:276px;top:660px;width:46px;background:#f7e3c7"></div>
  <div class="abs badge" style="left:328px;top:658px;width:50px;background:#8aa0c8"></div>
  <div class="abs badge" style="left:386px;top:659px;width:52px;background:#e5e5e5"></div>
  <div class="abs badge" style="left:118px;top:695px;width:48px;background:#dde6b4"></div>
  <div class="abs badge" style="left:182px;top:686px;width:42px;height:32px;background:#f3e5d2"></div>
  <div class="abs badge" style="left:230px;top:697px;width:70px;background:#e9e9e9"></div>
  <div class="abs badge" style="left:307px;top:696px;width:60px;background:#111"></div>

  <!-- footer -->
  <footer class="abs footer">
    <div class="abs foot-col" style="left:14px;top:9px">
      <strong>Home</strong>
      <strong style="margin-top:2px">About</strong>
      <span class="sub">- Company accreditations</span><br>
      <span class="sub">- Instructors/assessors</span><br>
      <span class="sub">- Management admin</span><br>
      <span class="sub">- Testimonials</span>
      <strong style="margin-top:2px">Course Locations</strong>
    </div>
    <div class="abs foot-rule" style="left:118px;top:30px"></div>
    <div class="abs foot-col" style="left:129px;top:9px">
      <strong>Courses</strong>
      <span class="sub">- RTA Approved Driver Licence &amp; Endorsement Courses</span><br>
      <span class="sub">- Heavy Vehicle</span><br>
      <span class="sub">- Light Vehicle Fleets</span><br>
      <span class="sub">- Forklifts</span><br>
      <span class="sub">- Plant &amp; Telehandler</span><br>
      <span class="sub">- Elevated Work Platforms / Scissor Lifts</span><br>
      <span class="sub">- Driving Instructors &amp; Assessors</span><br>
      <span class="sub">- Bus, Coach &amp; Taxi</span><br>
      <span class="sub">- Four Wheel Drive &amp; Quads</span><br>
      <span class="sub">- HazSub Approved Handler / Filler – Dangerous Goods Handling</span>
    </div>
    <div class="abs foot-rule" style="left:326px;top:30px"></div>
    <div class="abs foot-col" style="left:337px;top:11px;line-height:13px">
      <strong>Resources</strong>
      <strong>Links</strong>
      <strong>FAQs/ Enquiry</strong>
      <strong>Contact/Map</strong>
    </div>
    <div class="abs foot-map" role="img" aria-label="Map showing Australia and New Zealand"></div>
  </footer>
  <div class="abs copyright">© 2014 www.summitdriveacademy.example. All Rights Reserved</div>

</div>
</body>
</html>
```